Create Awesome Sale/AD graphics for BLACK FRIDAY

Create a (3) Black Friday graphics integrating our supplied pictures .
Text requirements = Black Friday/Cyber Monday sale
Text requirements = Deals up to 50% off
Text requirements = www.LAKOMBA.co
Integrate Lake Omba Logo

We would like to drop these graphics into a video, and use for Social Medai post's we would like perimeter around the graphic to be dark to fit the theme the graphic will be added at @15-17 sec in this video:
Youtube Video this Ad is live for this request here:
https://www.vidstreamo.example/watch?v=ZqT4mWbLr8e

I will upload a series of images we would like to use, choose the three you like to use.

Typically when we have graphics generated we get a zip file of the graphics in these formats EPS/AI/PDF/JPEG/PNG

Target Market(s)

Fishing, 50% mix male/female, ages 18-35

Colors

Designer to choose colors to be used in the design.

Requirements
Must have
• Create a (3) Black Friday graphics integrating our supplied pictures .
• Text requirements = Black Friday/Cyber Monday sale
• Text requirements = Deals up to 50% off
• Text requirements = www.LAKOMBA.co
• Integrate Lake Omba Logo
• ** I have more Lake Omba EPS/AI if needed See attached
Nice to have
• We would like to drop these graphics into a video, and use for Social Medai post's we would like perimeter around the graphic to be dark tto fit the theme the graphic will be added at @15-17 sec in this video:
• Youtube Video this Ad is live for this request here:
• https://www.vidstreamo.example/watch?v=ZqT4mWbLr8e
Should not have
• a lot of white space

```html
<!DOCTYPE html>
<html lang="en">
<head>
<meta charset="utf-8">
<title>Lake Omba – Super Black Friday Discount</title>
<link rel="stylesheet" href="https://fonts.googleapis.com/css2?family=Bebas+Neue&family=Roboto:wght@900&display=swap">
<style>
  :root {
    --bg-deep: #0d0f14;
    --bg-mid: #1b1e26;
    --bg-soft: #262a33;
    --red: #e3000b;
    --red-bright: #ff1a1a;
    --red-dark: #c70008;
    --white: #ffffff;
    --ink: #111111;
    --photo-light: #c4c6cb;
    --photo-mid: #8a8d94;
    --photo-dark: #3d4047;
    --photo-edge: #22252c;
  }
  * { box-sizing: border-box; margin: 0; padding: 0; }
  html, body {
    width: 1200px; height: 1200px; overflow: hidden;
    background: var(--bg-deep);
  }
  .ad {
    position: relative; width: 1200px; height: 1200px; overflow: hidden;
    background:
      linear-gradient(135deg, var(--bg-deep) 0%, var(--bg-mid) 35%, var(--bg-soft) 55%, var(--bg-mid) 75%, var(--bg-deep) 100%);
    font-family: "Bebas Neue", "Oswald", sans-serif;
    color: var(--white);
  }
  .frame-art { position: absolute; inset: 0; }
  .brand {
    position: absolute; left: 60px; top: 180px;
    font-size: 40px; letter-spacing: 9px; line-height: 1;
    color: var(--white);
  }
  .photo {
    position: absolute; left: 0; top: 440px; width: 880px; height: 760px;
    background:
      radial-gradient(ellipse 48% 18% at 48% 70%, var(--photo-light) 0%, var(--photo-mid) 60%, transparent 100%),
      radial-gradient(ellipse 30% 40% at 45% 32%, var(--photo-mid) 0%, var(--photo-dark) 70%, transparent 100%),
      linear-gradient(180deg, var(--photo-dark) 0%, #55585f 45%, var(--photo-dark) 80%, var(--photo-edge) 100%);
    border-radius: 0 48% 0 0 / 0 30% 0 0;
    -webkit-mask-image: linear-gradient(90deg, #000 80%, transparent 100%);
    mask-image: linear-gradient(90deg, #000 80%, transparent 100%);
  }
  .headline { position: absolute; left: 0; top: 0; width: 100%; }
  .headline span {
    position: absolute; display: block; text-align: center; line-height: 1;
    left: 799px; transform: translateX(-50%); white-space: nowrap;
  }
  .super    { top: 100px; font-size: 110px; }
  .black {
    top: 184px; font-size: 356px;
    background: linear-gradient(180deg, var(--red-bright) 0%, var(--red) 55%, var(--red-dark) 100%);
    -webkit-background-clip: text; background-clip: text; color: transparent;
    filter: drop-shadow(6px 6px 4px rgba(0,0,0,.7));
  }
  .friday   { top: 479px; font-size: 243px; filter: drop-shadow(5px 5px 4px rgba(0,0,0,.6)); }
  .discount { top: 697px; font-size: 90px; }
  .price-tag {
    position: absolute; left: 905px; top: 915px; width: 230px; height: 118px;
    transform: rotate(36deg); transform-origin: 50% 50%;
    background: var(--white);
    clip-path: polygon(0 50%, 22% 0, 100% 0, 100% 100%, 22% 100%);
    border-radius: 6px;
    font-family: "Roboto", "Arial Black", sans-serif; font-weight: 900;
  }
  .price-tag .hole {
    position: absolute; left: 24px; top: 52px; width: 14px; height: 14px;
    border-radius: 50%; background: var(--bg-mid);
  }
  .price-tag .amount {
    position: absolute; left: 52px; top: 8px; font-size: 92px; line-height: 1;
    color: var(--red); letter-spacing: -3px;
  }
  .price-tag .percent {
    position: absolute; left: 160px; top: 12px; font-size: 50px; line-height: 1; color: var(--ink);
  }
  .price-tag .off {
    position: absolute; left: 164px; top: 66px; font-size: 24px; line-height: 1; color: var(--ink);
  }
  .site-url {
    position: absolute; left: 908px; top: 1136px;
    font-size: 36px; letter-spacing: 1.5px; line-height: 1;
    text-transform: uppercase; color: var(--white);
  }
</style>
</head>
<body>
<main class="ad">
  <svg class="frame-art" width="1200" height="1200" viewBox="0 0 1200 1200" aria-hidden="true">
    <polygon class="diamond-shadow" points="800,30 1230,460 800,890 370,460" fill="#1a1d24" opacity=".85"/>
    <polygon class="diamond-outline" points="795,32 1208,445 795,858 381,445" fill="none" stroke="#d10009" stroke-width="4"/>
    <path class="tag-string" d="M801,853 C770,830 790,780 835,775 C880,772 875,805 840,812 C810,818 800,850 830,875 C860,900 900,915 935,925" fill="none" stroke="#e3000b" stroke-width="2"/>
  </svg>

  <div class="brand">Lake Omba</div>

  <div class="photo" role="img" aria-label="Black and white photo of an angler in a red cap and rain jacket holding a large salmon by the river"></div>

  <h1 class="headline">
    <span class="super">Super</span>
    <span class="black">Black</span>
    <span class="friday">Friday</span>
    <span class="discount">Discount</span>
  </h1>

  <div class="price-tag">
    <span class="hole"></span>
    <span class="amount">50</span>
    <span class="percent">%</span>
    <span class="off">OFF</span>
  </div>

  <p class="site-url">www.LAKOMBA.co</p>
</main>
</body>
</html>
```